4th Generation Family Business Needs a New Card Design!

We are a family owned 4th Generation company. We are based in the Sydney, Australia area and we are desperately in need of a more modern and classy card. We are monumental masons who design, supply & erect lasting memorials throughout cemeteries in Sydney. Our customers are normally in a period of grieving. I have attached logo files that will need to be implemented on the card. Company was established 1935. Australian Owned and Operated. Card needs to be designed to PRINTLY.com specification.

Target Market(s)

Our target market is based upon people that a grieving for family members that have passed away. We also deal with alot of companies that own and operate cemeteries.

Industry/Entity Type

Business

Contact Information for Business Card

Oliver Brantley, Operations Manager, 0417552908, oliver@hollowaystoneworks.com.au
Martin Brantley, Director, 0431906627, martin@hollowaystoneworks.com.au
Phone # 02 9634 2258
Website: www.hollowaystoneworks.com.au
Address: Suite 17, 8 Calloway Lane, East Penrose, Sydney NSW 2290

Font styles to use
Serif
Decorative
Script

Requirements
Must have
• Would like to see the logo nicely implemented with a modern design. Embossed lettering would be a nice additive.

```html
<!DOCTYPE html>
<html lang="en">
<head>
<meta charset="utf-8">
<title>Holloway Stoneworks – Business Card</title>
<link href="https://fonts.googleapis.com/css2?family=Roboto:wght@400;500&display=swap" rel="stylesheet">
<style>
  :root {
    --page-bg: #d9d9d9;
    --card-bg: #ffffff;
    --ink: #111111;
    --text-grey: #6a6a6a;
    --icon-gold: #dd9a2b;
    --accent-yellow: #e6cb3a;
    --deco-light: #f6f6f6;
    --deco-mid: #ececec;
  }
  * { margin: 0; padding: 0; box-sizing: border-box; }
  html, body {
    width: 1200px; height: 900px; overflow: hidden;
    background: var(--page-bg);
    font-family: "Roboto", Arial, sans-serif;
  }
  .card {
    position: absolute; left: 100px; top: 164px;
    width: 1000px; height: 572px;
    background: var(--card-bg);
    overflow: hidden;
    box-shadow: 0 18px 40px rgba(0,0,0,.25);
  }
  .card-art { position: absolute; inset: 0; }
  .brand {
    position: absolute; left: 540px; top: 150px;
    width: 270px;
    font-size: 32px; font-weight: 500; letter-spacing: 2px;
    color: var(--ink); text-transform: uppercase; line-height: 1.15;
    text-align: center;
  }
  .contact-list {
    position: absolute; left: 56px; top: 150px;
    list-style: none;
  }
  .contact-row {
    display: flex; align-items: center; gap: 22px;
    margin-bottom: 18px; min-height: 48px;
  }
  .icon {
    width: 46px; height: 46px; border-radius: 6px;
    background: var(--icon-gold);
    display: flex; align-items: center; justify-content: center;
    flex: none;
  }
  .icon svg { width: 26px; height: 26px; fill: #fff; }
  .contact-text {
    color: var(--text-grey); font-size: 19px; line-height: 1.3;
  }
</style>
</head>
<body>
  <main class="card">
    <svg class="card-art" width="1000" height="572" viewBox="0 0 1000 572">
      <defs>
        <linearGradient id="emblemTone" x1="0" y1="0" x2="1" y2="0">
          <stop offset="0" stop-color="var(--deco-light)"/>
          <stop offset="1" stop-color="var(--deco-mid)"/>
        </linearGradient>
      </defs>
      <rect class="emblem-decoration" x="840" y="0" width="160" height="572"
            fill="url(#emblemTone)" role="img"
            aria-label="Large cropped company emblem decoration"/>
      <polygon class="black-band" points="0,540 1000,290 1000,332 0,582" fill="var(--ink)"/>
    </svg>

    <div class="brand">Holloway<br>Stoneworks</div>

    <ul class="contact-list">
      <li class="contact-row">
        <span class="icon"><svg viewBox="0 0 24 24"><circle cx="12" cy="8" r="4.5"/><path d="M3 21c0-5 4-7.5 9-7.5s9 2.5 9 7.5z"/></svg></span>
        <span class="contact-text">Oliver Brantley<br>Operations Manager</span>
      </li>
      <li class="contact-row">
        <span class="icon"><svg viewBox="0 0 24 24"><path d="M3 9c0-3 4-5 9-5s9 2 9 5l-4 1-1-3H8L7 10zM6 11h12l2 9H4z"/><circle cx="12" cy="15" r="2.3" fill="#dd9a2b"/></svg></span>
        <span class="contact-text">0417552908</span>
      </li>
      <li class="contact-row">
        <span class="icon"><svg viewBox="0 0 24 24"><path d="M12 2a10 10 0 100 20 10 10 0 000-20zm0 2c1.5 1.5 2.5 4.5 2.5 8S13.5 18.5 12 20c-1.5-1.5-2.5-4.5-2.5-8S10.5 5.5 12 4zM4.2 11h15.6v2H4.2z" fill-rule="evenodd"/></svg></span>
        <span class="contact-text">oliver@hollowaystoneworks.com.au<br>www.hollowaystoneworks.com.au</span>
      </li>
      <li class="contact-row">
        <span class="icon"><svg viewBox="0 0 24 24"><path d="M12 3l10 9h-3v9h-5v-6h-4v6H5v-9H2z"/></svg></span>
        <span class="contact-text">Suite 17, 8 Calloway Lane,<br>East Penrose, Sydney NSW 2290</span>
      </li>
    </ul>
  </main>
</body>
</html>
```